lanternox munchies snack packaging

We are a new startup snack company that need a design for a snack packaging. Our snack goes by the name of lanternox munchies. Its a traditional snack usually eaten during festive seasons in south east asia region. The idea is to revolutionize the notion of the snack from one that is eaten during these celebratory seasons to an everyday one. The packaging design should be modern and minimalist yet fun too, also taking into consideration that it should not appear to be too childish. It should stand out from the other snacks products like potato chips etc if placed on the same shelf. The colour scheme is not decided yet as we are open to more ideas but colours should be complementary and not more than 2 or 3 hopefully. There should be also be an enthic sense of south east asian features on the design and it should reflects the Chinese, Malay and indian heritage. It need not be too obvious, a subtle kind should suffice. The packaging should also have the particular graphic/shape of the mould that i have upload followed by the picture of the snack. I have included a mock up of the logo of my company. Proposed designs can feel free to alter the lanternox graphic to a more modern, minimalist yet whimsical and fun. Proposed designs should have a front and back view of the packaging. We are looking to launch at 4 to 5 flavours like white sesame, black sesame, peanuts with white sesame and original.
Updates

Project Deadline Extended
Reason: Not enough submissions coming in yet.

Project Deadline Extended
Reason: Extension of deadline to allow more designs to come in.

Target Market(s)

All ages from as young as 5 to 6 years old to 60 to 70s.

Industry/Entity Type

It Company

Font styles to use
Other font styles liked:
• Fonts should be simple and minimalist. Easy for elderly to read without straining the eyes.

Requirements
Must have
• My logo which I have designed. Designers can feel free to tweak and enhance the design of the logo. The colour is not definite yet. Consumers must know what
• we are selling from the design of the packaging without guessing how it look
• like. The suggested packaging dimension is 17cm (W) by 23.5cm (H).
Nice to have
• We are looking to print the package using kraft paper which I have attached.
Should not have
• religious inclination of motifs, logo etc.

```html
<!DOCTYPE html>
<html lang="en">
<head>
<meta charset="utf-8">
<title>lanternox munchies – pouch front and back</title>
<link rel="stylesheet" href="https://fonts.googleapis.com/css2?family=Patrick+Hand&family=Ma+Shan+Zheng&family=Roboto+Condensed:wght@400;700&family=Roboto:wght@700&display=swap">
<style>
  :root{
    --bg:#ffffff;
    --kraft:#c8ab88;
    --kraft-light:#d4b995;
    --kraft-dark:#b89a76;
    --red:#b3121d;
    --red-deep:#9a0c16;
    --ink:#ffffff;
    --hanzi:#5a4a44;
  }
  *{margin:0;padding:0;box-sizing:border-box}
  html,body{width:1200px;height:788px;overflow:hidden;background:var(--bg)}
  .canvas{position:relative;width:1200px;height:788px}

  .pouch{position:absolute;top:27px;width:478px;height:720px;
    background:linear-gradient(180deg,var(--kraft-light) 0%,var(--kraft) 40%,var(--kraft-dark) 100%);
    border-radius:22px 22px 8px 8px}
  .pouch--front{left:90px}
  .pouch--back{left:660px}
  .pouch__seal{position:absolute;left:0;right:0;top:82px;height:2px;background:rgba(255,255,255,.25)}

  .brand-disc{position:absolute;border-radius:50%;
    background:radial-gradient(circle at 40% 35%,var(--red) 0%,var(--red-deep) 100%);
    display:flex;flex-direction:column;align-items:center;justify-content:center;
    color:var(--ink);font-family:'Patrick Hand',cursive;line-height:1}
  .brand-disc--front{left:44px;top:130px;width:410px;height:410px}
  .brand-disc--front .brand-name__line1{font-size:58px;letter-spacing:4px}
  .brand-disc--front .brand-name__line2{font-size:76px;margin-top:4px}
  .brand-disc--back{left:150px;top:70px;width:184px;height:184px}
  .brand-disc--back .brand-name__line1{font-size:26px;letter-spacing:2px}
  .brand-disc--back .brand-name__line2{font-size:34px;margin-top:2px}

  .hanzi-name{position:absolute;left:168px;top:560px;font-family:'Ma Shan Zheng',serif;
    font-size:40px;line-height:48px;color:var(--hanzi);letter-spacing:8px}

  .panel{position:absolute;background:var(--red);color:var(--ink);border:1.5px solid #fff}
  .nutrition{left:72px;top:276px;width:116px;height:386px;padding:5px 4px;
    font-family:'Roboto Condensed',sans-serif;font-size:6.4px;line-height:1.25}
  .nutrition h2{font-family:'Roboto',sans-serif;font-size:10.5px;border-bottom:1px solid #fff;padding-bottom:2px;margin-bottom:6px}
  .nutrition .rule{border-top:2.5px solid #fff;margin:3px 0}
  .nutrition .thin{border-top:.5px solid #fff;margin:2px 0}
  .nutrition .row{display:flex;justify-content:space-between}
  .nutrition b{font-size:7.2px}
  .nutrition .big{font-size:7.4px}
  .nutrition .pair{display:grid;grid-template-columns:1fr 1fr;gap:0 4px}
  .nutrition .note{font-size:4.6px;line-height:1.2;margin-top:3px}
  .nutrition table{width:100%;font-size:4.6px;border-collapse:collapse;margin-top:2px}
  .nutrition td{padding:0}

  .info{left:253px;top:276px;width:144px;height:322px;padding:5px 5px;
    font-family:'Roboto Condensed',sans-serif;font-size:6px;line-height:1.25}
  .info h3{font-size:8px;font-weight:700}
  .info .rule{border-top:1px solid #fff;margin:3px 0}
  .info .story{font-family:'Patrick Hand',cursive;font-size:9px;line-height:1.55;text-align:center;margin-top:18px}
  .info .story-zh{font-family:'Ma Shan Zheng',serif;font-size:9.5px;line-height:1.6;text-align:center;margin-top:14px}
  .info .contact{text-align:center;font-weight:700;font-size:7.5px;margin-top:24px}
  .info .links{text-align:center;font-size:6px;margin-top:8px;font-weight:700}
  .code-box{left:253px;top:602px;width:144px;height:60px;display:flex;align-items:center;justify-content:center;
    font-family:'Roboto Condensed',sans-serif;font-weight:700;font-size:20px}
</style>
</head>
<body>
<div class="canvas">

  <section class="pouch pouch--front" aria-label="Pouch front">
    <div class="pouch__seal"></div>
    <div class="brand-disc brand-disc--front">
      <span class="brand-name__line1">lanternox</span>
      <span class="brand-name__line2">munchies</span>
    </div>
    <p class="hanzi-name">灯笼<br>脆片</p>
  </section>

  <section class="pouch pouch--back" aria-label="Pouch back">
    <div class="pouch__seal"></div>
    <div class="brand-disc brand-disc--back">
      <span class="brand-name__line1">lanternox</span>
      <span class="brand-name__line2">munchies</span>
    </div>

    <div class="panel nutrition">
      <h2>Nutritional Facts</h2>
      <div>Serving Size 1 Package</div>
      <div>Serving Per Container 1</div>
      <div class="rule"></div>
      <div class="note">Amount Per Serving</div>
      <div class="thin"></div>
      <div class="big"><b>Calories 210</b></div>
      <div class="big"><b>Calories from Fat 110</b></div>
      <div class="thin"></div>
      <div class="row note"><span></span><span>% Daily Value</span></div>
      <div class="rule"></div>
      <div class="row"><b>Total Fat 13g</b><span></span></div>
      <div class="row"><span>Saturated Fat 2g</span><span>10%</span></div>
      <div class="row"><span>Trans Fat 0g</span><span>0%</span></div>
      <div class="thin"></div>
      <div class="row"><span><b>Cholesterol</b> 0mg</span><span>0%</span></div>
      <div class="row"><span><b>Sodium</b> 0mg</span><span>0%</span></div>
      <div class="row"><span><b>Potassium</b> 500mg</span><span>14%</span></div>
      <div class="row"><span><b>Total Carbohydrates</b> 22g</span><span>7%</span></div>
      <div>Dietary Fibre 2g</div>
      <div>Sugars 1g</div>
      <div><b>Protein</b> 3g</div>
      <div class="rule"></div>
      <div class="pair">
        <span>Vitamin A 0%</span><span>Vitamin C 15%</span>
        <span>Calcium 0%</span><span>Vitamin B6 15%</span>
        <span>Iron 4%</span><span>Phosphorus 6%</span>
        <span>Magnesium 8%</span><span>Zinc 2%</span>
      </div>
      <div class="thin"></div>
      <p class="note">* Percent Daily Values are based on a 2000 calorie diet. Your daily values may be higher or lower depending on your calorie needs.</p>
      <table>
        <tr><td></td><td>Calories</td><td>2000</td><td>2500</td></tr>
        <tr><td>Total Fat</td><td>Less than</td><td>65g</td><td>80g</td></tr>
        <tr><td>Sat Fat</td><td>Less than</td><td>20g</td><td>25g</td></tr>
        <tr><td>Cholesterol</td><td>Less than</td><td>300mg</td><td>300mg</td></tr>
        <tr><td>Sodium</td><td>Less than</td><td>2400mg</td><td>2400mg</td></tr>
        <tr><td>Potassium</td><td></td><td>3500mg</td><td>3500mg</td></tr>
        <tr><td>Total Carbohydrate</td><td></td><td>300g</td><td>375g</td></tr>
        <tr><td>Dietary Fibre</td><td></td><td>25g</td><td>30g</td></tr>
      </table>
      <p class="note">Calories per gram: Fat 9 · Carbohydrate 4 · Protein 4</p>
    </div>

    <div class="panel info">
      <h3>Ingredients:</h3>
      <div>Flour, Rice Flour, Sugar, Coconut Milk, Eggs, Vegetable Oil, Salt, Sesame Seeds</div>
      <div class="rule"></div>
      <h3>Manufactured By :</h3>
      <div><b>XXXXXXXXXXXXXX<br>XXXXXXXXXXXXXX</b></div>
      <div class="rule"></div>
      <p class="story">All our munchies are hand fry to perfection. Each one made with love, care and also that traditional flavour you are familiar with</p>
      <p class="story-zh">每一个脆片都是用手精心的烘烤。每一片都充满了温馨和你熟悉的味道。</p>
      <p class="contact">If interested in distributing<br>please call:<br>96100452/98300716</p>
      <p class="links">Like us @<br>www.snackpage.example/lanternox<br>or<br>Visit us @<br>www.lanternoxsnacks.example</p>
    </div>

    <div class="panel code-box">BARCODE</div>
  </section>

</div>
</body>
</html>
```